front and back labels on a single sheet.

Vodka label design
Vodka is a colourless liquor. This vodka is tasteless and with no flavour.

FRONT LABEL
"FROST TALLY" is the brand name . it should be as big as possible.
below that " Only vodka made from sustainable means"
Remaining details to be copied from attached file.
Back Label
Details attached.

Colors
00AB8E
00BBA5
67D7C9
C6EFE9
E9F9F6

```html
<!DOCTYPE html>
<html lang="en">
<head>
<meta charset="utf-8">
<title>Frost Tally – Vodka Labels</title>
<link href="https://fonts.googleapis.com/css2?family=Poppins:wght@400;500;600;700;800&display=swap" rel="stylesheet">
<style>
  :root{
    --sheet:#cfcfcf;
    --label:#ffffff;
    --green-deep:#1d6a27;
    --green-mid:#2f8f3a;
    --lime:#b9e24f;
    --lime-soft:#d2ee7a;
    --charcoal:#2e2e2e;
    --ink:#333333;
    --warn:#d8262c;
    --pattern-a:#f2f2f2;
    --pattern-b:#e4e4e4;
  }
  *{box-sizing:border-box;margin:0;padding:0}
  html,body{width:1200px;height:734px;overflow:hidden}
  body{background:var(--sheet);font-family:"Poppins",sans-serif;color:var(--ink)}
  .sheet{position:relative;width:1200px;height:734px;display:flex;justify-content:center;align-items:center;gap:60px}
  .label{position:relative;width:480px;height:580px;background:var(--label);overflow:hidden;box-shadow:0 6px 22px rgba(0,0,0,.18)}
  .leaf-field{position:absolute;left:0;right:0;background:linear-gradient(160deg,var(--pattern-a),var(--pattern-b) 55%,var(--pattern-a))}
  .lime-band{position:absolute;left:0;right:0;background:linear-gradient(90deg,var(--lime),var(--lime-soft));border-top:3px solid var(--green-mid);display:flex;align-items:center;justify-content:center;font-weight:700;color:var(--charcoal);letter-spacing:.3em}
  .dark-band{position:absolute;left:0;right:0;background:var(--charcoal);color:#fff;display:flex;align-items:center;justify-content:center;font-weight:600;letter-spacing:.3em}

  /* front */
  .front .leaf-field{top:140px;height:315px}
  .maker{position:absolute;top:52px;left:0;right:0;display:flex;align-items:center;justify-content:center;gap:8px}
  .maker-dot{width:14px;height:14px;border-radius:50%;background:var(--green-mid)}
  .maker-name{font-weight:700;font-size:20px;color:var(--green-deep);letter-spacing:.06em}
  .front-title{position:absolute;top:178px;left:0;right:0;text-align:center;color:var(--green-deep);font-weight:800;line-height:.9}
  .front-title .line1{display:block;font-size:104px;letter-spacing:-4px}
  .front-title .line2{display:block;font-size:84px;letter-spacing:-3px;color:var(--green-mid)}
  .front-claim{position:absolute;top:388px;left:0;right:0;text-align:center;color:var(--charcoal);font-weight:700;line-height:1.05}
  .front-claim .small{display:block;font-size:18px}
  .front-claim .big{display:block;font-size:25px}
  .front .lime-band{top:455px;height:46px;font-size:17px}
  .front .lime-band .sep{display:inline-block;width:2px;height:22px;background:var(--charcoal);margin:0 14px}
  .front .dark-band{top:501px;height:56px;font-size:16px}

  /* back */
  .back .leaf-field{top:128px;height:307px}
  .back-title{position:absolute;top:26px;left:0;right:0;text-align:center;color:var(--green-deep);font-weight:800;line-height:.92}
  .back-title .line1{display:block;font-size:54px;letter-spacing:-2px}
  .back-title .line2{display:block;font-size:46px;letter-spacing:-2px;color:var(--green-mid)}
  .story{position:absolute;top:160px;left:28px;right:28px;text-align:center;font-size:10.5px;line-height:1.35}
  .story p+p{margin-top:9px;text-align:justify;text-align-last:center}
  .notice-row{position:absolute;top:262px;left:56px;right:56px;height:48px;display:flex;align-items:center;gap:20px;border-top:1px solid #9a9a9a;border-bottom:1px solid #9a9a9a}
  .portrait{width:60px;height:60px;border-radius:50%;border:2px solid #555;background:radial-gradient(circle,#a77a5c,#5b3d2c);flex:none;margin-left:-28px}
  .warning{display:flex;align-items:center;gap:6px}
  .warning-title{color:var(--warn);font-weight:700;font-size:7.5px}
  .warning-text{font-size:6.5px;line-height:1.15;width:90px}
  .drinks-badge{width:28px;height:30px;border:1.5px solid #333;border-radius:3px 3px 8px 8px;margin-left:auto}
  .serving{position:absolute;top:340px;left:54px;width:172px;border:1px solid #555;border-radius:8px;padding:7px 10px;font-size:8px;line-height:1.25}
  .serving p+p{margin-top:5px}
  .producer{position:absolute;top:336px;left:250px;font-size:8px;line-height:1.3}
  .producer h4{color:var(--green-mid);font-size:8.5px;font-weight:700}
  .producer h4.gap{margin-top:6px}
  .back .lime-band{top:435px;height:46px;font-size:16px;letter-spacing:.22em}
  .back .dark-band{top:481px;height:56px;font-size:16px}
</style>
</head>
<body>
<main class="sheet">
  <section class="label front">
    <div class="maker"><span class="maker-dot"></span><span class="maker-name">VERDANT STILL</span></div>
    <div class="leaf-field" role="img" aria-label="Faint pattern of grey herb leaves"></div>
    <h1 class="front-title"><span class="line1">FROST</span><span class="line2">TALLY</span></h1>
    <p class="front-claim"><span class="small">ONLY VODKA MADE FROM</span><span class="big">SUSTAINABLE MEANS</span></p>
    <div class="lime-band">50% ABV<span class="sep"></span>750ML</div>
    <div class="dark-band">PREMIUM QUALITY VODKA</div>
  </section>

  <section class="label back">
    <h2 class="back-title"><span class="line1">FROST</span><span class="line2">TALLY</span></h2>
    <div class="leaf-field" role="img" aria-label="Faint pattern of grey herb leaves"></div>
    <div class="story">
      <p>The only vodka in the whole world which has unique 5 spices, and distrilled 3+1 times</p>
      <p>In addition this is the only vodka made from natutral rainwater &amp; solar power, thus making it the only vodka that is sustainably manufactured.</p>
    </div>
    <div class="notice-row">
      <div class="portrait" role="img" aria-label="Portrait photo of the master distiller"></div>
      <div class="warning">
        <svg width="24" height="24" viewBox="0 0 24 24" aria-hidden="true"><circle cx="12" cy="12" r="10" fill="none" stroke="#333" stroke-width="2"/><line x1="5" y1="19" x2="19" y2="5" stroke="#333" stroke-width="2"/></svg>
        <div><div class="warning-title">PREGNANCY WARNING</div><div class="warning-text">Alcohol can cause lifelong harm to your baby</div></div>
      </div>
      <svg width="30" height="26" viewBox="0 0 30 26" aria-hidden="true"><path d="M15 2 L28 24 H2 Z" fill="none" stroke="#333" stroke-width="1.5"/><path d="M10 18 h10" stroke="#333" stroke-width="1.3"/></svg>
      <div class="drinks-badge"></div>
    </div>
    <div class="serving">
      <p>This vodka has to be taken chilled with ice cubes</p>
      <p>Making cocktails with lime and orange is a wonderful experience.</p>
    </div>
    <div class="producer">
      <h4>FERMENTED AND DISTRILLED BY</h4>
      <p>MASTER R. ELLIS MORAN<br>AT VERDANT STILL PVT. LTD.</p>
      <h4 class="gap">MADE IN</h4>
      <p>ASHVALE, VICTORIA<br>AUSTRALIA</p>
    </div>
    <div class="lime-band">www.verdantstill.com.au</div>
    <div class="dark-band">MADE FROM SUGARCANE</div>
  </section>
</main>
</body>
</html>
```